Sydney law firm, Prestwicks Solicitors, needs a flyer design!

We need a flyer design for our law firm which has been operating in Sydney for over 35 years. We want to send the flyer out to potential clients and also to existing clients to let them know the range of services that we provide. Our corporate colours are white, red and black and we would like these incorporated somewhat. The final design should be clean, modern and professional.

We would like the design to fit a double sided flyer approx. 210mm high x 100mm wide.

Industry/Entity Type

Law Firm

Font styles to use
Serif
Sans Serif

Colors
eb2026
ffffff

Requirements
Must have
• Details needed on the flyer are:
• Prestwicks Solicitors
• 3/82 Carradine Street, Liverpool, NSW 2170
• (02) 9418 3562
• www.prestwickssolicitors-example.com.au
• info@prestwickssolicitors-example.com.au
• Our areas of practice include:
• Property Law
• Conveyancing
• Leases
• Criminal Law
• Family Law
• Litigation and Dispute Resolution
• Company Law
• Wills and Estates
• Powers of Attorney and Guardianship
Should not have
• a picture of scales or a picture of a gavel

```html
<!DOCTYPE html>
<html lang="en">
<head>
<meta charset="utf-8">
<title>Prestwicks Solicitors – Practice Areas Flyer</title>
<link rel="stylesheet" href="https://fonts.googleapis.com/css2?family=Cinzel:wght@500;600&family=Oswald:wght@300;500&family=Cormorant+SC:wght@500&display=swap">
<style>
  :root {
    --canvas-bg: #ece9e3;
    --ink: #1d1d1d;
    --paper: #ffffff;
    --paper-shade: #d9d9d9;
    --logo-band: #dcdcdc;
    --logo-band-light: #ececec;
    --footer: #454545;
    --footer-dark: #3a3a3a;
    --footer-text: #ffffff;
    --footer-muted: #e2e2e2;
    --brand-red: #eb2026;
  }
  * { box-sizing: border-box; margin: 0; padding: 0; }
  html, body {
    width: 1200px; height: 1000px; overflow: hidden;
    background: var(--canvas-bg);
  }
  .flyer {
    position: absolute;
    left: 362px; top: 18px;
    width: 455px; height: 955px;
    display: flex; flex-direction: column;
    box-shadow: 0 2px 8px rgba(0,0,0,.18);
  }
  .services {
    height: 672px;
    background: radial-gradient(ellipse 75% 45% at 50% 55%, var(--paper) 55%, var(--paper-shade) 100%);
    list-style: none;
    display: flex; flex-direction: column; align-items: center;
    padding-top: 44px;
    gap: 25px;
  }
  .services li {
    font-family: "Cinzel", serif;
    font-weight: 600;
    font-size: 24px;
    line-height: 30px;
    color: var(--ink);
    text-align: center;
    letter-spacing: .5px;
  }
  .services li.long { max-width: 360px; }
  .identity {
    height: 138px;
    background: linear-gradient(180deg, var(--logo-band-light), var(--logo-band));
    border-top: 1px solid #c8c8c8;
    display: flex; align-items: center; justify-content: center;
  }
  .firm-name {
    font-family: "Cinzel", serif;
    font-weight: 500;
    font-size: 33px;
    color: var(--ink);
    letter-spacing: 1px;
  }
  .contact {
    flex: 1;
    background: linear-gradient(180deg, var(--footer), var(--footer-dark));
    color: var(--footer-text);
    text-align: center;
    padding-top: 16px;
  }
  .contact .phone {
    font-family: "Cormorant SC", serif;
    font-weight: 500;
    font-size: 27px;
    line-height: 30px;
  }
  .contact .web {
    font-family: "Oswald", sans-serif;
    font-weight: 500;
    font-size: 21px;
    line-height: 32px;
    letter-spacing: -.2px;
  }
  .contact .address, .contact .email {
    font-family: "Cormorant SC", serif;
    font-size: 14px;
    line-height: 15px;
    color: var(--footer-muted);
  }
  .contact .address { margin-top: 6px; }
</style>
</head>
<body>
  <article class="flyer">
    <ul class="services">
      <li>Property Law</li>
      <li>Conveyancing</li>
      <li>Leases</li>
      <li>Criminal Law</li>
      <li>Family Law</li>
      <li class="long">Litigation and Dispute Resolution</li>
      <li>Company Law</li>
      <li>Wills and Estates</li>
      <li class="long">Powers of Attorney and Guardianship</li>
    </ul>
    <header class="identity">
      <h1 class="firm-name">Prestwicks Solicitors</h1>
    </header>
    <footer class="contact">
      <p class="phone">(02) 9418 3562</p>
      <p class="web">www.prestwickssolicitors-example.com.au</p>
      <p class="address">3/82 Carradine Street, Liverpool, NSW 2170</p>
      <p class="email">info@prestwickssolicitors-example.com.au</p>
    </footer>
  </article>
</body>
</html>
```